Large Financial Advisory Firm Needs a Brochure!

We are looking for a modern and professional 4 page brochure for our Financial Advisory firm, Heronfield Capital Partners. I've attached multiple files to help with the completion of the design.
SIZE OF BROCHURE: 17 x 11 FLAT, 8.5 x 11 inch FOLDED
1. A PDF titled Design Brief will provide you with an overview of the project, the text to be included in the brochure and other misc. instructions.
2. Logo Files, you will need to incorporate our logo into the brochure design, I've attached all the files please select the images that suit your design.
3. Competitor Illustration - I've attached an image that needs to be included on the 2nd page (inside left cover of the brochure). You will need to incorporate the pros/cons of using our competitors and the advantages of using our firm. This is outlined in the Design Brief PDF.
NOTE: If possible please get rid of the blue sky in the illustration. Just use the buildings, the blue throws off the concept. I contacted the illustrator and am waiting for a design without the sky but it may not be ready in time so please delete it if possible.
- I like the Avenir fonts, 85 Heavy, 65 Medium and 45.

```html
<!DOCTYPE html>
<html lang="en">
<head>
<meta charset="utf-8">
<title>Heronfield Capital Partners – Brochure Spread</title>
<link href="https://fonts.googleapis.com/css2?family=Cinzel:wght@500;600&family=Questrial&display=swap" rel="stylesheet">
<style>
  :root{
    --gold:#fbbd2e;
    --ink:#000000;
    --paper:#ffffff;
    --backdrop:#e6e6e6;
    --photo-light:#f4f4f4;
    --photo-mid:#c9c9c9;
    --rule:#9a8a60;
  }
  *{margin:0;padding:0;box-sizing:border-box}
  html,body{width:1200px;height:824px;overflow:hidden;background:var(--backdrop)}
  .spread{
    position:absolute;left:20px;top:38px;width:1420px;height:916px;
    transform:scale(.817);transform-origin:0 0;
    font-family:"Questrial",sans-serif;
    box-shadow:0 4px 18px rgba(0,0,0,.25);
  }
  /* inside page: team */
  .team-page{position:absolute;left:0;top:0;width:710px;height:916px;background:var(--ink);color:var(--paper)}
  .team-header{position:absolute;left:0;top:42px;width:710px;height:49px;background:var(--gold);
    display:flex;align-items:center;justify-content:center}
  .team-header h1{font-family:"Cinzel",serif;font-weight:600;font-size:25px;color:var(--ink);letter-spacing:.5px}
  .bio{position:absolute;left:63px;width:582px}
  .bio h2{font-size:18.5px;font-weight:400;color:var(--gold);letter-spacing:.1px;-webkit-text-stroke:.4px var(--gold)}
  .bio .role{font-size:13.5px;color:var(--gold);margin-top:4px;margin-bottom:10px}
  .bio p{font-size:11.6px;line-height:13.95px;text-align:justify;letter-spacing:.05px}
  .bio p + p{margin-top:14px}
  .bio-martin{top:111px}
  .bio-colin{top:358px}
  .bio-owen{top:591px}
  .team-footer{position:absolute;left:0;top:816px;width:710px;height:60px;background:var(--gold)}
  .footer-brand{position:absolute;left:54px;top:795px;width:102px;height:110px;background:var(--ink);
    display:flex;flex-direction:column;align-items:center;justify-content:center;gap:8px;text-align:center}
  .footer-brand .mark{width:22px;height:22px;background:var(--gold)}
  .footer-brand .name{font-size:12px;line-height:13px;color:var(--gold)}
  .contacts{position:absolute;left:162px;top:816px;height:60px;display:flex;align-items:center;gap:16px;color:var(--ink);font-size:12.5px}
  .contacts span{display:flex;align-items:center;gap:5px}
  .contacts .phone{font-size:16px;font-weight:400;-webkit-text-stroke:.5px var(--ink)}
  /* cover page */
  .cover-page{position:absolute;left:710px;top:0;width:710px;height:916px;background:var(--gold)}
  .cover-photo{position:absolute;left:0;top:0;width:710px;height:528px;
    background:radial-gradient(ellipse at 75% 60%,var(--photo-light) 0%,#e2e2e2 45%,var(--photo-mid) 100%)}
  .cover-rule{position:absolute;left:0;top:528px;width:710px;height:5px;
    background:linear-gradient(90deg,#222,var(--rule) 60%,#ddd)}
  .cover-brand{position:absolute;left:1240px;left:500px;top:640px;width:200px;text-align:center;
    display:flex;flex-direction:column;align-items:center;gap:14px;color:var(--ink)}
  .cover-brand .mark{width:40px;height:40px;background:var(--ink)}
  .cover-brand .name{font-size:21px;line-height:24px;letter-spacing:.5px}
  .tagline-band{position:absolute;left:0;top:816px;width:710px;height:60px;background:var(--ink);
    display:flex;align-items:center;justify-content:center}
  .tagline-band h2{font-family:"Cinzel",serif;font-weight:500;font-size:33px;color:var(--paper);letter-spacing:1.2px}
</style>
</head>
<body>
<div class="spread">
  <section class="team-page">
    <header class="team-header"><h1>Our Team</h1></header>

    <article class="bio bio-martin">
      <h2>Martin Avery, CFA, CPA</h2>
      <div class="role">Founder</div>
      <p>Martin works collaboratively with advisors to formulate successful transition plans. He brings creative insight and deep experience to this niche industry that is sorely lacking in both. Prior to his current role, Martin worked at Stonebridge Fund Advisors where he rose quickly to Regional Director and developed relationships with advisors throughout the Western US. He loved his role at the firm, but became frustrated when some of his closest clients struggled to find the right partner for succession. He witnessed deals implode due to cultural, philosophical, and operational differences and in some cases firms gave up their succession search altogether. He founded Heronfield Capital Partners to make sure advisors find the succession partner they deserve.</p>
      <p>Martin earned a bachelor's degree in Finance from Northgate University. He is a Certified Public Accountant and a CFA Charterholder. Martin enjoys spending time with his wife Helena, traveling internationally, studying foreign languages, and staying active.</p>
    </article>

    <article class="bio bio-colin">
      <h2>Colin Reyes, CFA</h2>
      <div class="role">Founder</div>
      <p>Colin has over ten years of experience in the financial services industry. Prior to joining Heronfield Capital Partners, he has served as Portfolio Manager and research analyst for various financial service companies, both large and small. Colin wears multiple hats for the organization; he leads the portfolio management team, oversees our operations staff and handles the technological integration between firms. He has been involved in multiple Advisor mergers and transitions and understands the challenges that firms face when looking for a succession partner. Colin grew up in Southern California and earned a BA from Linwood University where he studied Public Policy, Economics and German. He holds the Chartered Financial Analyst (CFA) designation.</p>
      <p>Colin enjoys spending his coveted free time with his wife Maren and 4 young children.<br>Colin's hobbies include martial arts, reading, cooking, and taking interesting MOOC courses.</p>
    </article>

    <article class="bio bio-owen">
      <h2>Owen Reyes</h2>
      <div class="role">Founder</div>
      <p>Owen brings over 10 years of M&amp;A experience to Heronfield Capital Partners. His expertise in deal structure, operational management, and corporate finance allow him to design customized succession plans for advisors. Owen is previously experienced in commercial finance, in 1998 he co-founded Keystone Lending; and serving as President and Managing Member, built a 100+ employee &amp; $35mm revenue equipment leasing company, which he sold in July 2008. Owen attended Westmere College and earned a Bachelor of Arts degree in English Literature while obtaining a minor in Economics and Communications.</p>
      <p>Owen and his wife Clara have 4 active young children. Owen's hobbies include competing in triathlons throughout the United States, traveling, gourmet cooking, and spending time with family.</p>
    </article>

    <div class="team-footer"></div>
    <div class="footer-brand">
      <div class="mark"></div>
      <div class="name">Heronfield Capital Partners</div>
    </div>
    <div class="contacts">
      <span><svg width="13" height="10" viewBox="0 0 13 10"><rect x=".75" y=".75" width="11.5" height="8.5" fill="none" stroke="#000" stroke-width="1.5"/><path d="M1 1l5.5 4.5L12 1" fill="none" stroke="#000" stroke-width="1.5"/></svg>martin.avery@heronfieldcp.com</span>
      <span class="phone"><svg width="15" height="15" viewBox="0 0 16 16"><circle cx="8" cy="8" r="7" fill="none" stroke="#000" stroke-width="1.4"/><path d="M6 4.5c-1 1-1 3.5 1 5.5s4 2.5 5 1.5l-1.3-1.5-1.2.6c-1-.5-2-1.6-2.4-2.5l.7-1.2z" fill="#000"/></svg>555-014-2273</span>
      <span><svg width="11" height="11" viewBox="0 0 12 12"><circle cx="6" cy="6" r="5.2" fill="none" stroke="#000" stroke-width="1.3"/><path d="M1 6h10M6 1c-2.5 3-2.5 7 0 10M6 1c2.5 3 2.5 7 0 10" fill="none" stroke="#000" stroke-width="1"/></svg>www.heronfieldcp.com</span>
    </div>
  </section>

  <section class="cover-page">
    <div class="cover-photo" role="img" aria-label="Photograph: a row of glossy grey spheres on a curved white track, with one red sphere standing apart"></div>
    <div class="cover-rule"></div>
    <div class="cover-brand">
      <div class="mark"></div>
      <div class="name">Heronfield Capital Partners</div>
    </div>
    <div class="tagline-band"><h2>Redefining Investment Advice</h2></div>
  </section>
</div>
</body>
</html>
```